Swimming pool service business postcard redesign

We need a fresh post card design for our pool service business based in San Diego called Tide Buffers. We are a family based, local residential pool cleaning and maintenance company. we need an offer to stand out, our logo, our colors, etc on a 5.5x8 inch full color post card.

```html
<!DOCTYPE html>
<html lang="en">
<head>
<meta charset="utf-8">
<title>Tide Buffers – Pool Service Postcard</title>
<link rel="stylesheet" href="https://fonts.googleapis.com/css2?family=Oswald:wght@400;500;600;700&family=Montserrat:wght@500;600&family=Yellowtail&family=Great+Vibes&display=swap">
<style>
  :root {
    --navy: #0b3a7e;
    --deep: #063e7f;
    --mid-blue: #0f56a3;
    --sky: #1c8be0;
    --pale: #cfe6f8;
    --cyan: #3bb5ec;
    --red: #e8231f;
    --white: #ffffff;
  }
  * { margin: 0; padding: 0; box-sizing: border-box; }
  html, body { width: 1200px; height: 825px; overflow: hidden; background: #fff; }
  .postcard { position: relative; width: 1200px; height: 825px; overflow: hidden; font-family: "Oswald", sans-serif; }
  .backdrop { position: absolute; inset: 0; }
  .abs { position: absolute; }

  .brand { left: 50px; top: 150px; display: flex; align-items: center; gap: 18px; }
  .brand-dot { width: 54px; height: 54px; border-radius: 50%; background: var(--red); }
  .brand-name { color: var(--white); font-weight: 700; font-size: 66px; line-height: 1; text-transform: uppercase; letter-spacing: 1px; }

  .headline-script { left: 590px; top: 58px; white-space: nowrap; font-family: "Yellowtail", cursive; color: var(--navy); font-size: 34px; line-height: 1; transform: rotate(-11deg); transform-origin: left bottom; }
  .headline-main { left: 535px; top: 104px; height: 70px; white-space: nowrap; font-weight: 700; color: var(--navy); font-size: 58px; line-height: 70px; letter-spacing: 1px; transform: rotate(-10deg); transform-origin: left bottom; }
  .tagline { left: 636px; top: 160px; width: 342px; height: 50px; background: var(--red); transform: rotate(-9deg);
    color: var(--white); font-weight: 600; font-size: 22px; white-space: nowrap; display: flex; align-items: center; justify-content: center; }

  .values-title { left: 0; width: 470px; top: 430px; text-align: center; font-weight: 700; color: var(--navy); font-size: 38px; }
  .values-sub { left: 0; width: 470px; top: 478px; text-align: center; font-family: "Montserrat", sans-serif; font-weight: 500; color: var(--navy); font-size: 15.5px; }
  .values { left: 20px; top: 522px; width: 420px; display: flex; }
  .value { flex: 1; text-align: center; color: var(--navy); font-weight: 500; font-size: 15px; line-height: 1.35; border-left: 2px solid #fff; }
  .value:first-child { border-left: none; }
  .value svg { width: 54px; height: 54px; display: block; margin: 0 auto 20px; }
  .values-script { left: 0; width: 470px; top: 640px; text-align: center; font-family: "Great Vibes", cursive; color: var(--navy); font-size: 34px; }

  .services-label { left: 492px; top: 402px; width: 232px; height: 40px; background: var(--cyan); color: #fff; font-size: 25px; display: flex; align-items: center; justify-content: center; border-radius: 4px; }
  .services { left: 505px; top: 450px; list-style: none; color: #fff; font-size: 19px; }
  .services li { display: flex; align-items: center; gap: 10px; height: 25.5px; }
  .services svg { width: 22px; height: 22px; flex: none; }
  .services-script { left: 515px; top: 632px; font-family: "Great Vibes", cursive; color: #fff; font-size: 25px; line-height: 1.2; }

  .coupon { left: 780px; top: 360px; width: 402px; height: 335px; background: #fff; border-radius: 22px; }
  .coupon-frame { position: absolute; inset: 13px; border: 3px dashed var(--sky); border-radius: 16px; }
  .coupon-banner { position: absolute; left: 52px; top: 26px; width: 298px; height: 27px; background: var(--red); color: #fff; font-weight: 600; font-size: 23px; text-align: center; line-height: 27px; }
  .coupon-amount { position: absolute; left: 36px; top: 58px; color: var(--red); font-weight: 700; display: flex; }
  .coupon-amount .dollar { font-size: 56px; margin-top: 2px; }
  .coupon-amount .num { font-size: 118px; line-height: 1; letter-spacing: -3px; margin-left: 4px; }
  .coupon-amount .off { font-size: 66px; line-height: 1; margin-left: 36px; margin-top: 4px; }
  .coupon-wave { position: absolute; left: 240px; top: 136px; width: 126px; height: 20px; }
  .coupon-lead { position: absolute; left: 0; width: 100%; top: 180px; text-align: center; color: var(--navy); font-weight: 700; line-height: 1.05; }
  .coupon-lead .l1 { font-size: 28px; display: block; }
  .coupon-lead .l2 { font-size: 34px; display: block; }
  .coupon-body { position: absolute; left: 0; width: 100%; top: 246px; text-align: center; color: var(--navy); font-family: "Montserrat", sans-serif; font-size: 15.5px; line-height: 1.35; }
  .coupon-terms { position: absolute; left: 0; width: 100%; top: 296px; text-align: center; color: var(--navy); font-family: "Montserrat", sans-serif; font-size: 9.5px; }

  .footer-cta { left: 44px; top: 733px; width: 221px; height: 64px; background: var(--red); border-radius: 4px; display: flex; align-items: center; gap: 12px; padding-left: 18px; color: #fff; font-weight: 600; font-size: 21px; line-height: 1.05; }
  .footer-cta svg { width: 36px; height: 36px; flex: none; }
  .footer-item { display: flex; align-items: center; gap: 14px; color: #fff; }
  .footer-item .ico { width: 36px; height: 36px; border-radius: 50%; background: #fff; display: flex; align-items: center; justify-content: center; flex: none; }
  .footer-item .ico svg { width: 22px; height: 22px; }
  .phone { left: 310px; top: 735px; }
  .phone-num { font-size: 40px; font-weight: 500; line-height: 1; }
  .phone-alt { font-size: 20px; text-align: right; line-height: 1; }
  .web { left: 600px; top: 744px; font-size: 29px; }
  .area { left: 878px; top: 740px; font-size: 26px; line-height: 1.2; }
  .divider { top: 740px; width: 2px; height: 56px; background: var(--red); }
</style>
</head>
<body>
<div class="postcard">
  <svg class="backdrop" viewBox="0 0 1200 825" width="1200" height="825" aria-hidden="true">
    <defs>
      <linearGradient id="topBlue" x1="0" y1="0" x2="1" y2="1">
        <stop offset="0" stop-color="#1f8fe0"/><stop offset="1" stop-color="#0b4f9c"/>
      </linearGradient>
      <linearGradient id="lowerBlue" x1="0" y1="0" x2="1" y2="0">
        <stop offset="0" stop-color="#0a4a93"/><stop offset="1" stop-color="#1a86d8"/>
      </linearGradient>
    </defs>
    <rect width="1200" height="712" fill="url(#topBlue)"/>
    <rect y="340" width="1200" height="372" fill="url(#lowerBlue)"/>
    <path d="M0,400 C120,370 300,352 470,362 V712 H0 Z" fill="var(--pale)"/>
    <path d="M350,0 C420,30 440,90 420,150" fill="none" stroke="#fff" stroke-width="12"/>
    <rect y="712" width="1200" height="113" fill="var(--deep)"/>
    <path d="M135,506 C200,500 280,500 333,505" stroke="var(--red)" stroke-width="2" fill="none"/>
    <path d="M172,695 C240,686 310,686 370,692" stroke="var(--red)" stroke-width="2" fill="none"/>
    <path d="M560,705 C620,696 670,696 716,702" stroke="var(--red)" stroke-width="2" fill="none"/>
  </svg>

  <svg class="abs" style="left:0;top:0" width="1200" height="400" viewBox="0 0 1200 400" role="img" aria-label="Photo of a resort pool with lounge chairs, umbrella and tropical plants">
    <defs>
      <linearGradient id="poolScene" x1="0" y1="0" x2="0" y2="1">
        <stop offset="0" stop-color="#dfeef3"/><stop offset="0.45" stop-color="#8fbf8a"/><stop offset="0.75" stop-color="#43b6c2"/><stop offset="1" stop-color="#2a8fb0"/>
      </linearGradient>
    </defs>
    <path d="M418,0 H1200 V365 L780,388 C690,382 560,352 470,360 L395,372 C425,270 445,150 418,0 Z" fill="url(#poolScene)"/>
  </svg>

  <div class="abs brand"><span class="brand-dot"></span><span class="brand-name">Tide<br>Buffers</span></div>

  <div class="abs headline-script">Keeping San Diego Pools</div>
  <div class="abs headline-main">SPARKLING CLEAN!</div>
  <div class="abs tagline">SO YOU CAN RELAX &amp; ENJOY!</div>

  <div class="abs values-title">FAMILY. LOCAL. TRUSTED.</div>
  <div class="abs values-sub">Proudly serving San Diego and surrounding areas.</div>
  <div class="abs values">
    <div class="value">
      <svg viewBox="0 0 54 54" fill="none" stroke="var(--navy)" stroke-width="3"><circle cx="34" cy="18" r="10"/><path d="M29 18l4 4 6-7"/><path d="M4 44l10-10h14l6-4 8-3-10 10H18" stroke-linejoin="round"/></svg>
      RELIABLE<br>SERVICE
    </div>
    <div class="value">
      <svg viewBox="0 0 54 54" fill="var(--navy)"><circle cx="20" cy="6" r="4"/><rect x="14" y="22" width="26" height="10" rx="3"/><path d="M10 34h34l4 14H6z"/></svg>
      SPARKLING<br>CLEAN POOLS
    </div>
    <div class="value">
      <svg viewBox="0 0 54 54"><circle cx="20" cy="16" r="12" fill="var(--navy)"/><circle cx="33" cy="38" r="12" fill="var(--navy)"/><text x="20" y="22" font-size="16" fill="#fff" text-anchor="middle" font-family="Oswald">$</text><text x="33" y="44" font-size="16" fill="#fff" text-anchor="middle" font-family="Oswald">$</text></svg>
      AFFORDABLE<br>PRICING
    </div>
    <div class="value">
      <svg viewBox="0 0 54 54" fill="none" stroke="var(--navy)" stroke-width="3"><circle cx="27" cy="27" r="24"/><path d="M12 28l15-13 15 13v14H12z" stroke-linejoin="round"/><circle cx="27" cy="30" r="5"/></svg>
      FAMILY<br>OWNED
    </div>
  </div>
  <div class="abs values-script">We treat your pool like our own!</div>

  <div class="abs services-label">OUR SERVICES</div>
  <ul class="abs services">
    <li><svg viewBox="0 0 22 22"><path d="M2 12l6 7L20 3" fill="none" stroke="var(--red)" stroke-width="3"/></svg>Weekly Pool Cleaning</li>
    <li><svg viewBox="0 0 22 22"><path d="M2 12l6 7L20 3" fill="none" stroke="var(--red)" stroke-width="3"/></svg>Equipment Inspection</li>
    <li><svg viewBox="0 0 22 22"><path d="M2 12l6 7L20 3" fill="none" stroke="var(--red)" stroke-width="3"/></svg>Water Balancing</li>
    <li><svg viewBox="0 0 22 22"><path d="M2 12l6 7L20 3" fill="none" stroke="var(--red)" stroke-width="3"/></svg>Filter Cleaning</li>
    <li><svg viewBox="0 0 22 22"><path d="M2 12l6 7L20 3" fill="none" stroke="var(--red)" stroke-width="3"/></svg>Tile &amp; Surface Brushing</li>
    <li><svg viewBox="0 0 22 22"><path d="M2 12l6 7L20 3" fill="none" stroke="var(--red)" stroke-width="3"/></svg>Skimmer &amp; Pump Checks</li>
    <li><svg viewBox="0 0 22 22"><path d="M2 12l6 7L20 3" fill="none" stroke="var(--red)" stroke-width="3"/></svg>Reliable &amp; Consistent Care</li>
  </ul>
  <div class="abs services-script">Let us handle the work,<br>so you can enjoy your pool!</div>

  <div class="abs coupon">
    <div class="coupon-frame"></div>
    <div class="coupon-banner">NEW CUSTOMER OFFER</div>
    <div class="coupon-amount"><span class="dollar">$</span><span class="num">50</span><span class="off">OFF</span></div>
    <svg class="coupon-wave" viewBox="0 0 126 20"><path d="M2 14 Q17 2 32 12 T62 12 T92 12 T124 12" fill="none" stroke="var(--navy)" stroke-width="5"/></svg>
    <div class="coupon-lead"><span class="l1">YOUR FIRST MONTH OF</span><span class="l2">POOL SERVICE!</span></div>
    <div class="coupon-body">Schedule today and let us take<br>pool care off your plate.</div>
    <div class="coupon-terms">Not valid with other offers. One per household. Expires 9/30/25.</div>
  </div>

  <div class="abs footer-cta">
    <svg viewBox="0 0 36 36" fill="#fff"><rect x="2" y="6" width="32" height="28" rx="2"/><rect x="5" y="14" width="26" height="17" fill="var(--red)"/><g fill="#fff"><rect x="7" y="16" width="5" height="4"/><rect x="15" y="16" width="5" height="4"/><rect x="23" y="16" width="5" height="4"/><rect x="7" y="23" width="5" height="4"/><rect x="15" y="23" width="5" height="4"/><rect x="23" y="23" width="5" height="4"/></g></svg>
    <span>SCHEDULE YOUR<br>FREE ESTIMATE!</span>
  </div>
  <div class="abs footer-item phone">
    <span class="ico"><svg viewBox="0 0 24 24"><path d="M6.6 10.8a15 15 0 006.6 6.6l2.2-2.2a1 1 0 011-.25 11.4 11.4 0 003.6.6 1 1 0 011 1V20a1 1 0 01-1 1A17 17 0 013 4a1 1 0 011-1h3.5a1 1 0 011 1c0 1.25.2 2.45.6 3.6a1 1 0 01-.25 1z" fill="var(--deep)"/></svg></span>
    <div><div class="phone-num">619-555-TIDE</div><div class="phone-alt">(8433)</div></div>
  </div>
  <div class="abs divider" style="left:581px"></div>
  <div class="abs footer-item web">
    <span class="ico"><svg viewBox="0 0 24 24"><path d="M6.6 10.8a15 15 0 006.6 6.6l2.2-2.2a1 1 0 011-.25 11.4 11.4 0 003.6.6 1 1 0 011 1V20a1 1 0 01-1 1A17 17 0 013 4a1 1 0 011-1h3.5a1 1 0 011 1c0 1.25.2 2.45.6 3.6a1 1 0 01-.25 1z" fill="var(--deep)"/></svg></span>
    <span>TideBuffersSD.com</span>
  </div>
  <div class="abs divider" style="left:853px"></div>
  <div class="abs footer-item area">
    <span class="ico"><svg viewBox="0 0 24 24"><path d="M12 3L2 12h3v8h5v-5h4v5h5v-8h3z" fill="var(--deep)"/></svg></span>
    <span>Proudly Serving San<br>Diego &amp; Surrounding Areas</span>
  </div>
</div>
</body>
</html>
```